Criação de Power Point Slide Mestre para Consultoria de Negócios
" Com os meus conhecimentos profissionais (acadêmicos e por experiência), procuro identificar no mercado em quais empresas posso oferecer os meus serviços. Procuro passar a imagem de que a consultoria é algo que não "algema" a empresa e tampouco a pune por erros já cometidos. Procuro sempre deixar claro que a consultoria não executa as ações, ela conversa com a gestão e essa sim é que decide se a proposta da consultoria vai ao encontro dos objetivos dos proprietários. Costumo ressaltar que a consultoria é a teoria a serviço da pratica na gestão. Gestão e Controles são palavras de ordem. "

```html
<!DOCTYPE html>
<html lang="pt-BR">
<head>
<meta charset="UTF-8">
<title>Slide Mestre – Vértice Consultoria</title>
<link href="https://fonts.googleapis.com/css2?family=Open+Sans:wght@400;600;700&display=swap" rel="stylesheet">
<style>
  :root {
    --navy: #1d3764;
    --navy-deep: #14284d;
    --navy-light: #2d4f86;
    --white: #ffffff;
    --mist: #c9ced6;
    --photo-dark: #3a3f48;
    --photo-mid: #7c8492;
    --photo-light: #d7dbe1;
    --page: #f2f2f2;
  }
  * { box-sizing: border-box; margin: 0; padding: 0; }
  html, body {
    width: 1200px; height: 1200px; overflow: hidden;
    background: var(--page);
    font-family: "Open Sans", Arial, sans-serif;
  }
  .slide {
    position: absolute; left: 40px; top: 285px;
    width: 1120px; height: 630px;
    overflow: hidden;
    background: var(--white);
    box-shadow: 0 6px 24px rgba(0,0,0,0.12);
  }
  .slide__photo {
    position: absolute; inset: 0;
    background:
      radial-gradient(ellipse at 30% 75%, var(--photo-light) 0%, transparent 45%),
      radial-gradient(ellipse at 85% 30%, var(--photo-light) 0%, transparent 35%),
      linear-gradient(160deg, var(--photo-mid) 0%, var(--photo-dark) 55%, var(--photo-mid) 100%);
  }
  .slide__veil {
    position: absolute; left: 40px; top: 100px;
    width: 1040px; height: 300px;
    background: rgba(120,128,140,0.55);
  }
  .brand {
    position: absolute; left: 26px; top: 22px;
    width: 150px; height: 68px;
    background: var(--white);
    display: flex; align-items: center; gap: 8px;
    padding: 0 10px;
  }
  .brand__mark { width: 16px; height: 16px; background: var(--navy); flex: none; }
  .brand__name {
    font-size: 13px; font-weight: 700; color: var(--navy);
    line-height: 1.15; text-transform: uppercase;
  }
  .title-band {
    position: absolute; left: 370px; top: 30px;
    width: 750px; height: 56px;
    background: var(--navy);
    border-left: 8px solid var(--navy-light);
    display: flex; align-items: center; padding-left: 28px;
  }
  .title-band__text {
    color: var(--white); font-size: 27px; font-weight: 700;
    letter-spacing: 0.5px; text-transform: uppercase;
  }
  .content {
    position: absolute; left: 70px; top: 112px; width: 980px;
    color: var(--white);
  }
  .content__subtitle { font-size: 38px; font-weight: 400; margin-bottom: 14px; }
  .content__body {
    font-size: 16.5px; line-height: 1.45; text-align: justify;
    text-indent: 40px; margin-bottom: 16px; font-weight: 600;
  }
  .swoosh { position: absolute; left: 0; top: 0; width: 1120px; height: 630px; }
</style>
</head>
<body>
  <main class="slide">
    <div class="slide__photo" role="img" aria-label="Fotografia de mãos montando peças de quebra-cabeça, em tons de cinza e azul"></div>
    <div class="slide__veil"></div>

    <svg class="swoosh" viewBox="0 0 1120 630" aria-hidden="true">
      <path d="M560 630 C 760 560, 960 430, 1120 250 L1120 630 Z" fill="var(--mist)"/>
      <path d="M600 630 C 790 570, 975 450, 1120 285 L1120 630 Z" fill="var(--white)"/>
      <path d="M640 630 C 820 580, 990 470, 1120 320 L1120 630 Z" fill="var(--navy)"/>
    </svg>

    <div class="brand">
      <span class="brand__mark"></span>
      <span class="brand__name">Vértice<br>Consultoria</span>
    </div>

    <header class="title-band">
      <h1 class="title-band__text">Título do Slide</h1>
    </header>

    <section class="content">
      <h2 class="content__subtitle">Subtítulo (se houver)</h2>
      <p class="content__body">Sed ut perspiciatis unde omnis iste natus error sit voluptatem accusantium doloremque laudantium, totam rem aperiam, eaque ipsa quae ab illo inventore veritatis et quasi architecto beatae vitae dicta sunt explicabo. Nemo enim ipsam voluptatem quia voluptas sit aspernatur aut odit aut fugit, sed quia consequuntur magni dolores eos qui ratione voluptatem sequi nesciunt.</p>
      <p class="content__body">Neque porro quisquam est, qui dolorem ipsum quia dolor sit amet, consectetur, adipisci velit, sed quia non numquam eius modi tempora incidunt ut labore et dolore magnam aliquam quaerat voluptatem.</p>
    </section>
  </main>
</body>
</html>
```